Design Creative Banner or Gif Ads. 3 Designs To Be Selected

Come up with some creative banner ads for stonewell.co.nz

*At least 3 different winning banners will be chosen*

Please provide banner ads / gif ads in common google ads / website banner formats.

They can be gif or static but must stand out while still maintaining clear clean text and visuals, with a premium professional feel (please avoid clip art or anything that gives a cheap message).

Please keep in mind that these will likely be small ads so text needs to be large and if there's there a lot of text then use multiple frames/ pages as submit as a gif.

Style
Minimal & clean lines
Architectural or realistic images
Avoid cartoon styles, clipart, or anything that looks cheap

Font
Nexa or Montserrat or similar

Tone
Premium, serious, trustworthy — fits new builds

Colours
Option 1: Deep Navy (trust & quality) & lighter blues and warm grey
Option 2: Open to bright colours to help the ads stand out, such as (but not limited to) bright pink with black, yellow, fluorescent green, provided the messaging is still done professionally.
Our logo is attached (Stone Well Logo)

Display Sizes
Ad specs for file sizes should be file formats like JPEG, GIF, and PNG, with animations limited to a max of 30 seconds or less.
We will need several different ad sizes provided for each of the 3 selected winning designs.

• Medium Rectangle: 300 × 250 pixels
• Leaderboard: 728 × 90 pixels
• Desktop Banner ad image: (640x360 pixels)
• Desktop Banner ad image 2: (300x600 pixels)
• Possibly one or two other sizes

Flexibility to be creative
The ad text, words, upper/lower case, layout, colour, theme, and images can be adjusted to how you think it will look best. The follow example ads are just examples of what we are after but we are keen to see what you can create.

Recommendations at this point:
1. Avoid text heavy
2. Looking for more Gif ads
3. Imaging: if possible use real stock photo's rather than AI

Themes:

1
Building Soon? Start Here
Free Build Planning Pack:
✓ Build Cost Calculator
✓ Hidden Cost Checklist
✓ Builder Comparison Guide
Build With Confidence
Download Free

2
Before You Choose A Builder
Compare Price, Scope, Risk & Value
Avoid Costly Mistakes
Choose The Right Builder With Confidence
Download The Free Guide

3
Planning A New Build?
Avoid These Common Mistakes:
✗ Hidden Exclusions
✗ Missing Scope
✗ Unrealistic Allowances
✗ Budget Blowouts
Download The Free Guide

4
Before You Buy Land
Know what it could cost to build.
Avoid Costly Building Mistakes
Download Our Free Guides

5
Know Your Build Budget?
• Free Build Cost Calculator
• Hidden Cost Checklist
• Build Planning Tools
Calculate Costs (Download)

Target Market(s)

Landowners looking to build

Industry/Entity Type

Building

Font styles to use
Other font styles liked:
• Nexa or Montserrat or similar

Requirements
Should not have
• Avoid cartoon styles, clipart, or anything that looks cheap

```html
<!DOCTYPE html>
<html lang="en">
<head>
<meta charset="utf-8">
<title>Stone Well – Know Your Build Budget? Banner Set</title>
<link href="https://fonts.googleapis.com/css2?family=Montserrat:wght@500;600;700;800&display=swap" rel="stylesheet">
<style>
  :root{
    --board:#b3b3b3;
    --panel:#f5fbfd;
    --navy:#0f3550;
    --blue:#36a0c9;
    --green:#38c46a;
    --green-dark:#27944f;
    --white:#ffffff;
  }
  *{box-sizing:border-box;margin:0;padding:0}
  html,body{width:1200px;height:784px;overflow:hidden;background:var(--board)}
  body{position:relative;font-family:"Montserrat",sans-serif;color:var(--navy)}
  .ad{position:absolute;background:var(--panel);overflow:hidden}
  .ad > svg.shapes{position:absolute;left:0;top:0;width:100%;height:100%}
  .abs{position:absolute}
  .headline{font-weight:800;line-height:1.2;letter-spacing:-0.2px}
  .navy{color:var(--navy)} .blue{color:var(--blue)}
  .chevrons{position:absolute;fill:var(--blue)}
  .brand{position:absolute;display:flex;align-items:center}
  .brand-mark{background:var(--navy);flex:none}
  .brand-text{display:flex;flex-direction:column}
  .brand-name{font-weight:600;color:var(--navy);line-height:1;white-space:nowrap}
  .brand-tag{font-weight:600;color:var(--blue);text-transform:uppercase;white-space:nowrap;letter-spacing:.1px;margin-top:2px}
  .checks{position:absolute;list-style:none;font-weight:700;color:var(--navy)}
  .checks li{display:flex;align-items:center;white-space:nowrap}
  .tick{flex:none;fill:none;stroke:var(--blue);stroke-width:3;stroke-linecap:round;stroke-linejoin:round}
  .cta{position:absolute;display:flex;align-items:center;justify-content:center;background:var(--green);color:var(--white);font-weight:700;border-radius:6px;border-bottom:3px solid var(--green-dark);white-space:nowrap}
  .footer-bar{position:absolute;left:0;bottom:0;width:100%;height:8px;background:var(--navy)}
</style>
</head>
<body>

<svg width="0" height="0" style="position:absolute" aria-hidden="true">
  <defs>
    <linearGradient id="site-photo" x1="0" y1="0" x2="0" y2="1">
      <stop offset="0" stop-color="#eef2f3"/>
      <stop offset="0.25" stop-color="#3b4049"/>
      <stop offset="0.55" stop-color="#b98d5e"/>
      <stop offset="0.78" stop-color="#8d6b4b"/>
      <stop offset="1" stop-color="#7a5c40"/>
    </linearGradient>
  </defs>
</svg>

<!-- Desktop banner 640x360 : headline -->
<section class="ad" style="left:136px;top:55px;width:448px;height:251px">
  <svg class="shapes" viewBox="0 0 448 251" preserveAspectRatio="none">
    <rect x="215" y="90" width="233" height="161" fill="url(#site-photo)" role="img" aria-label="Photo of a modern black-clad gable home beside a timber-framed build on site"/>
    <polygon points="204,0 242,0 203,126 242,251 204,251 165,126" fill="var(--blue)"/>
  </svg>
  <svg class="chevrons" style="left:152px;top:26px;width:24px;height:20px" viewBox="0 0 24 20"><polygon points="0,0 5,0 11,10 5,20 0,20 6,10"/><polygon points="11,0 16,0 22,10 16,20 11,20 17,10"/></svg>
  <div class="brand" style="left:246px;top:24px;gap:9px">
    <span class="brand-mark" style="width:30px;height:30px"></span>
    <span class="brand-text"><span class="brand-name" style="font-size:20px">Stone Well</span><span class="brand-tag" style="font-size:5px">Compare quotes from trusted builders</span></span>
  </div>
  <h1 class="headline abs" style="left:27px;top:67px;font-size:30px;line-height:37px">
    <span class="navy">Know</span><br><span class="navy">Your</span><br><span class="blue">Build</span><br><span class="blue">Budget?</span>
  </h1>
</section>

<!-- Desktop banner 640x360 : checklist -->
<section class="ad" style="left:704px;top:55px;width:445px;height:251px">
  <svg class="shapes" viewBox="0 0 445 251" preserveAspectRatio="none">
    <rect x="215" y="90" width="230" height="161" fill="url(#site-photo)" role="img" aria-label="Photo of a modern black-clad gable home beside a timber-framed build on site"/>
    <polygon points="204,0 242,0 203,126 242,251 204,251 165,126" fill="var(--blue)"/>
  </svg>
  <svg class="chevrons" style="left:153px;top:26px;width:24px;height:20px" viewBox="0 0 24 20"><polygon points="0,0 5,0 11,10 5,20 0,20 6,10"/><polygon points="11,0 16,0 22,10 16,20 11,20 17,10"/></svg>
  <div class="brand" style="left:246px;top:24px;gap:9px">
    <span class="brand-mark" style="width:30px;height:30px"></span>
    <span class="brand-text"><span class="brand-name" style="font-size:20px">Stone Well</span><span class="brand-tag" style="font-size:5px">Compare quotes from trusted builders</span></span>
  </div>
  <ul class="checks" style="left:17px;top:51px;font-size:11.5px">
    <li style="height:23px;gap:6px"><svg class="tick" width="12" height="11" viewBox="0 0 12 11"><polyline points="1.5,6 4.5,9.5 10.5,1.5"/></svg>Free Build Cost Calculator</li>
    <li style="height:23px;gap:6px"><svg class="tick" width="12" height="11" viewBox="0 0 12 11"><polyline points="1.5,6 4.5,9.5 10.5,1.5"/></svg>Hidden Cost Checklist</li>
    <li style="height:23px;gap:6px"><svg class="tick" width="12" height="11" viewBox="0 0 12 11"><polyline points="1.5,6 4.5,9.5 10.5,1.5"/></svg>Build Planning Tools</li>
  </ul>
  <div class="cta" style="left:28px;top:162px;width:123px;height:41px;font-size:13px">Calculate Costs</div>
</section>

<!-- Leaderboard 728x90 : headline -->
<section class="ad" style="left:136px;top:334px;width:506px;height:63px">
  <svg class="shapes" viewBox="0 0 506 63" preserveAspectRatio="none">
    <polygon points="0,0 80,0 88,31 80,63 0,63" fill="url(#site-photo)" role="img" aria-label="Photo of a modern home and timber-framed build"/>
    <polygon points="75,0 85,0 94,31 85,63 75,63 84,31" fill="var(--blue)"/>
  </svg>
  <svg class="chevrons" style="left:469px;top:10px;width:18px;height:15px" viewBox="0 0 24 20"><polygon points="0,0 5,0 11,10 5,20 0,20 6,10"/><polygon points="11,0 16,0 22,10 16,20 11,20 17,10"/></svg>
  <p class="headline abs" style="left:121px;top:18px;font-size:21px;white-space:nowrap"><span class="navy">Know Your </span><span class="blue">Build Budget?</span></p>
</section>

<!-- Leaderboard 728x90 : checklist -->
<section class="ad" style="left:136px;top:413px;width:506px;height:62px">
  <svg class="shapes" viewBox="0 0 506 62" preserveAspectRatio="none">
    <polygon points="0,0 80,0 88,31 80,62 0,62" fill="url(#site-photo)" role="img" aria-label="Photo of a modern home and timber-framed build"/>
    <polygon points="75,0 85,0 94,31 85,62 75,62 84,31" fill="var(--blue)"/>
  </svg>
  <svg class="chevrons" style="left:469px;top:10px;width:18px;height:15px" viewBox="0 0 24 20"><polygon points="0,0 5,0 11,10 5,20 0,20 6,10"/><polygon points="11,0 16,0 22,10 16,20 11,20 17,10"/></svg>
  <ul class="checks" style="left:119px;top:16px;font-size:12.5px">
    <li style="gap:3px"><svg class="tick" width="13" height="12" viewBox="0 0 12 11"><polyline points="1.5,6 4.5,9.5 10.5,1.5"/></svg>Build Planning Tools</li>
  </ul>
  <ul class="checks" style="left:294px;top:16px;font-size:12.5px">
    <li style="gap:3px"><svg class="tick" width="13" height="12" viewBox="0 0 12 11"><polyline points="1.5,6 4.5,9.5 10.5,1.5"/></svg>Hidden Cost Checklist</li>
  </ul>
  <ul class="checks" style="left:207px;top:36px;font-size:12.5px">
    <li style="gap:3px"><svg class="tick" width="13" height="12" viewBox="0 0 12 11"><polyline points="1.5,6 4.5,9.5 10.5,1.5"/></svg>Build Planning Tools</li>
  </ul>
</section>

<!-- Leaderboard 728x90 : brand + CTA -->
<section class="ad" style="left:136px;top:492px;width:506px;height:62px">
  <svg class="shapes" viewBox="0 0 506 62" preserveAspectRatio="none">
    <polygon points="0,0 80,0 88,31 80,62 0,62" fill="url(#site-photo)" role="img" aria-label="Photo of a modern home and timber-framed build"/>
    <polygon points="75,0 85,0 94,31 85,62 75,62 84,31" fill="var(--blue)"/>
  </svg>
  <div class="brand" style="left:118px;top:15px;gap:10px">
    <span class="brand-mark" style="width:32px;height:32px"></span>
    <span class="brand-text"><span class="brand-name" style="font-size:18px">Stone Well</span><span class="brand-tag" style="font-size:4.5px">Compare quotes from trusted builders</span></span>
  </div>
  <div class="cta" style="left:349px;top:13px;width:107px;height:36px;font-size:11px">Calculate Costs</div>
</section>

<!-- Medium rectangle 300x250 : headline -->
<section class="ad" style="left:40px;top:571px;width:208px;height:174px">
  <svg class="shapes" viewBox="0 0 208 174" preserveAspectRatio="none">
    <rect x="50" y="74" width="158" height="100" fill="url(#site-photo)" role="img" aria-label="Photo of a modern black-clad gable home beside a timber-framed build"/>
    <polygon points="42,0 70,0 44,87 70,174 43,174 17,87" fill="var(--blue)"/>
  </svg>
  <svg class="chevrons" style="left:8px;top:152px;width:17px;height:14px" viewBox="0 0 24 20"><polygon points="0,0 5,0 11,10 5,20 0,20 6,10"/><polygon points="11,0 16,0 22,10 16,20 11,20 17,10"/></svg>
  <p class="headline abs" style="left:76px;top:28px;font-size:14.5px;line-height:18px"><span class="navy">Know Your</span><br><span class="blue">Build Budget?</span></p>
</section>

<!-- Medium rectangle 300x250 : checklist -->
<section class="ad" style="left:263px;top:571px;width:208px;height:174px">
  <svg class="shapes" viewBox="0 0 208 174" preserveAspectRatio="none">
    <rect x="50" y="74" width="158" height="100" fill="url(#site-photo)" role="img" aria-label="Photo of a modern black-clad gable home beside a timber-framed build"/>
    <polygon points="42,0 70,0 44,87 70,174 43,174 17,87" fill="var(--blue)"/>
  </svg>
  <svg class="chevrons" style="left:8px;top:152px;width:17px;height:14px" viewBox="0 0 24 20"><polygon points="0,0 5,0 11,10 5,20 0,20 6,10"/><polygon points="11,0 16,0 22,10 16,20 11,20 17,10"/></svg>
  <ul class="checks" style="left:69px;top:20px;font-size:10px;font-weight:600">
    <li style="height:18px;gap:2px"><svg class="tick" width="11" height="10" viewBox="0 0 12 11"><polyline points="1.5,6 4.5,9.5 10.5,1.5"/></svg>Hidden Cost Checklist</li>
    <li style="height:18px;gap:2px"><svg class="tick" width="11" height="10" viewBox="0 0 12 11"><polyline points="1.5,6 4.5,9.5 10.5,1.5"/></svg>Build Planning Tools</li>
    <li style="height:18px;gap:2px"><svg class="tick" width="11" height="10" viewBox="0 0 12 11"><polyline points="1.5,6 4.5,9.5 10.5,1.5"/></svg>Build Planning Tools</li>
  </ul>
</section>

<!-- Medium rectangle 300x250 : brand + CTA -->
<section class="ad" style="left:484px;top:571px;width:208px;height:174px">
  <svg class="shapes" viewBox="0 0 208 174" preserveAspectRatio="none">
    <rect x="50" y="74" width="158" height="100" fill="url(#site-photo)" role="img" aria-label="Photo of a modern black-clad gable home beside a timber-framed build"/>
    <polygon points="42,0 70,0 44,87 70,174 43,174 17,87" fill="var(--blue)"/>
  </svg>
  <svg class="chevrons" style="left:8px;top:152px;width:17px;height:14px" viewBox="0 0 24 20"><polygon points="0,0 5,0 11,10 5,20 0,20 6,10"/><polygon points="11,0 16,0 22,10 16,20 11,20 17,10"/></svg>
  <div class="brand" style="left:84px;top:14px;gap:7px">
    <span class="brand-mark" style="width:22px;height:22px"></span>
    <span class="brand-text"><span class="brand-name" style="font-size:12px">Stone Well</span><span class="brand-tag" style="font-size:3px">Compare quotes from trusted builders</span></span>
  </div>
  <div class="cta" style="left:100px;top:43px;width:72px;height:24px;font-size:8px;border-radius:4px;border-bottom-width:2px">Calculate Costs</div>
</section>

<!-- Half page 300x600 : checklist + CTA -->
<section class="ad" style="left:717px;top:328px;width:209px;height:417px">
  <svg class="shapes" viewBox="0 0 209 417" preserveAspectRatio="none">
    <polygon points="0,70 209,70 209,168 105,200 0,168" fill="url(#site-photo)" role="img" aria-label="Photo of a modern black-clad gable home beside a timber-framed build"/>
    <polygon points="0,168 105,200 209,168 209,200 105,231 0,200" fill="var(--blue)"/>
  </svg>
  <div class="brand" style="left:34px;top:21px;gap:9px">
    <span class="brand-mark" style="width:20px;height:20px"></span>
    <span class="brand-text"><span class="brand-name" style="font-size:15px">Stone Well</span><span class="brand-tag" style="font-size:4px">Compare quotes from trusted builders</span></span>
  </div>
  <svg class="chevrons" style="left:174px;top:232px;width:22px;height:18px" viewBox="0 0 24 20"><polygon points="0,0 5,0 11,10 5,20 0,20 6,10"/><polygon points="11,0 16,0 22,10 16,20 11,20 17,10"/></svg>
  <ul class="checks" style="left:12px;top:257px;font-size:12.5px">
    <li style="height:26px;gap:8px"><svg class="tick" width="13" height="12" viewBox="0 0 12 11"><polyline points="1.5,6 4.5,9.5 10.5,1.5"/></svg>Free Build Cost Calculator</li>
    <li style="height:26px;gap:8px"><svg class="tick" width="13" height="12" viewBox="0 0 12 11"><polyline points="1.5,6 4.5,9.5 10.5,1.5"/></svg>Hidden Cost Checklist</li>
    <li style="height:26px;gap:8px"><svg class="tick" width="13" height="12" viewBox="0 0 12 11"><polyline points="1.5,6 4.5,9.5 10.5,1.5"/></svg>Build Planning Tools</li>
  </ul>
  <div class="cta" style="left:27px;top:342px;width:157px;height:53px;font-size:17px;border-radius:8px;border-bottom-width:4px">Calculate Costs</div>
  <div class="footer-bar"></div>
</section>

<!-- Half page 300x600 : headline -->
<section class="ad" style="left:943px;top:328px;width:209px;height:417px">
  <svg class="shapes" viewBox="0 0 209 417" preserveAspectRatio="none">
    <polygon points="0,80 209,80 209,191 105,221 0,191" fill="url(#site-photo)" role="img" aria-label="Photo of a modern black-clad gable home beside a timber-framed build"/>
    <polygon points="0,191 105,221 209,191 209,221 105,251 0,221" fill="var(--blue)"/>
  </svg>
  <div class="brand" style="left:17px;top:25px;gap:11px">
    <span class="brand-mark" style="width:29px;height:29px"></span>
    <span class="brand-text"><span class="brand-name" style="font-size:19px">Stone Well</span><span class="brand-tag" style="font-size:4.5px">Compare quotes from trusted builders</span></span>
  </div>
  <svg class="chevrons" style="left:173px;top:266px;width:24px;height:20px" viewBox="0 0 24 20"><polygon points="0,0 5,0 11,10 5,20 0,20 6,10"/><polygon points="11,0 16,0 22,10 16,20 11,20 17,10"/></svg>
  <h2 class="headline abs" style="left:19px;top:266px;font-size:28px;line-height:37px">
    <span class="navy">Know</span><br><span class="navy">Your Build</span><br><span class="blue">Budget</span><span class="navy">?</span>
  </h2>
  <div class="footer-bar"></div>
</section>

</body>
</html>
```